Need high-end luxury business cards with raised element of logo

Looking for a non-standard business card with the option of part of our logo elements to be printed as raised or embossed. Would like at least 5 different photos on the backside. Looking at printing through this: https://www.cardvelo.com/raised-spot-uv-business-cards.html

updated the logo file

```html
<!DOCTYPE html>
<html lang="en">
<head>
<meta charset="utf-8">
<title>Larkmoor Row — Business Card</title>
<link href="https://fonts.googleapis.com/css2?family=Montserrat:wght@400;500;700&display=swap" rel="stylesheet">
<style>
  :root {
    --backdrop: #3b3b3d;
    --card: #141517;
    --card-edge: #5d7f98;
    --accent: #5d7f98;
    --ink: #e8e8e8;
    --gloss-dark: #121315;
    --gloss-light: #3a3c40;
  }
  * { margin: 0; padding: 0; box-sizing: border-box; }
  html, body {
    width: 1200px; height: 801px; overflow: hidden;
    background: var(--backdrop);
    font-family: "Montserrat", sans-serif;
  }
  .stage {
    position: relative; width: 1200px; height: 801px;
    display: flex; align-items: center; justify-content: center; gap: 60px;
  }
  .card {
    position: relative; width: 520px; height: 297px;
    background: var(--card);
    border-bottom: 2px solid var(--card-edge);
    border-right: 1px solid var(--card-edge);
    box-shadow: 0 18px 40px rgba(0,0,0,.45);
    overflow: hidden;
  }
  .brand-name {
    color: var(--accent); font-weight: 500;
    letter-spacing: .14em; text-transform: uppercase; line-height: 1;
  }
  .brand-sub {
    display: flex; align-items: center; gap: 10px;
    color: var(--accent); font-weight: 500; font-size: 9px; letter-spacing: .5em;
  }
  .brand-sub::before, .brand-sub::after {
    content: ""; flex: 1; height: 1px; background: var(--accent);
  }

  /* info side */
  .info .brand { position: absolute; left: 34px; top: 66px; width: 200px; }
  .info .brand-name { font-size: 26px; }
  .info .brand-sub { margin-top: 8px; }
  .divider { position: absolute; left: 0; right: 0; top: 140px; height: 1px; background: var(--accent); }
  .person { position: absolute; right: 34px; top: 74px; text-align: right; }
  .person-name { color: var(--accent); font-weight: 700; font-size: 17px; letter-spacing: .04em; }
  .person-role { color: var(--ink); font-size: 12px; margin-top: 6px; }
  .address { position: absolute; right: 34px; top: 166px; text-align: right; color: var(--ink); font-size: 13px; line-height: 1.6; }
  .contacts { position: absolute; left: 34px; bottom: 34px; list-style: none; color: var(--ink); font-size: 12px; }
  .contacts li { display: flex; align-items: center; gap: 9px; line-height: 1.85; }
  .contacts svg { width: 11px; height: 11px; fill: var(--accent); flex: none; }

  /* brand side */
  .brand-side .brand { position: absolute; left: 0; right: 0; top: 46px; text-align: center; }
  .brand-side .brand-name { font-size: 34px; }
  .brand-side .brand-sub { width: 240px; margin: 9px auto 0; }
  .raised-area {
    position: absolute; left: 0; right: 0; bottom: 0; height: 170px;
    background: linear-gradient(100deg, var(--gloss-dark) 0%, var(--gloss-dark) 35%, var(--gloss-light) 80%, #4a4c50 100%);
    opacity: .85;
  }
</style>
</head>
<body>
<main class="stage">

  <section class="card info" aria-label="Card contact side">
    <div class="brand">
      <div class="brand-name">Larkmoor</div>
      <div class="brand-sub">ROW</div>
    </div>
    <div class="person">
      <div class="person-name">OWEN CASTELL</div>
      <div class="person-role">President</div>
    </div>
    <div class="divider"></div>
    <div class="address">1180 Seabright Quay<br>Harbor Bay CA 90000</div>
    <ul class="contacts">
      <li><svg viewBox="0 0 24 24"><path d="M6.6 10.8a15 15 0 0 0 6.6 6.6l2.2-2.2c.3-.3.7-.4 1-.2 1.1.4 2.3.6 3.6.6.6 0 1 .4 1 1V20c0 .6-.4 1-1 1A17 17 0 0 1 3 4c0-.6.4-1 1-1h3.5c.6 0 1 .4 1 1 0 1.3.2 2.5.6 3.6.1.3 0 .7-.2 1z"/></svg>555-240-6180</li>
      <li><svg viewBox="0 0 24 24"><path d="M2 5h20v14H2z M2 5l10 8 10-8" /></svg>owen@larkmoorrow.com</li>
      <li><svg viewBox="0 0 24 24"><circle cx="12" cy="12" r="10"/></svg>www.larkmoorrow.com</li>
    </ul>
  </section>

  <section class="card brand-side" aria-label="Card brand side">
    <div class="brand">
      <div class="brand-name">Larkmoor</div>
      <div class="brand-sub">ROW</div>
    </div>
    <div class="raised-area" role="img" aria-label="Raised gloss spot UV decorative artwork area"></div>
  </section>

</main>
</body>
</html>
```